Business Card design for a skin clinic

i would like a business card design for our skin clinic.
our logo colors are Blue and Grey and Bule /white.
we are searching for a minimalistic design yet very elegant,dynamic and professional which can reflect a professional medical skin care clinic( not a beauty salon).
THE DESGIN IS NOT FOR A PERSON IT WILL BE USED IN THE CLINIC FOR CLIENTS SO THERE SHOULD BE NO NAME OF A PERSON ONLY THE CLINIC NAME AND THE CONTACT INFO

Target Market(s)
young and old womens
Industry/Entity Type
Business
Contact Information for Business Card
we have 2 address and both should be on the card.
address A: Lindenhoflaan 214B, 3041KP Rotterdam, Tel 010 483 21 95
address B: Zonnewijzerstraat 238, 1062RT Amsterdam Tel 020 571 3829
website www.huidpuntzorg.nu, email info@huidpuntzorg.nu
Look and feel
Each slider illustrates characteristics of the customer's brand and the style your logo design should communicate.

```html
<!DOCTYPE html>
<html lang="nl">
<head>
<meta charset="utf-8">
<title>Huidpuntzorg – visitekaartje</title>
<link href="https://fonts.googleapis.com/css2?family=Roboto+Condensed:wght@300;400&display=swap" rel="stylesheet">
<style>
  :root {
    --page: #ffffff;
    --card-dark: #1a1f28;
    --card-light: #fdfdfd;
    --brand-light: #dfe3e8;
    --tagline: #c3c7cc;
    --ink: #1b1b1b;
    --shadow: rgba(0, 0, 0, 0.16);
  }
  * { margin: 0; padding: 0; box-sizing: border-box; }
  html, body {
    width: 1200px;
    height: 1200px;
    overflow: hidden;
    background: var(--page);
    font-family: "Roboto Condensed", sans-serif;
  }
  .sheet { position: relative; width: 1200px; height: 1200px; }
  .card {
    position: absolute;
    left: 203px;
    width: 794px;
    height: 520px;
  }
  .card--front { top: 68px; background: var(--card-dark); }
  .card--back {
    top: 611px;
    background: var(--card-light);
    box-shadow: 0 10px 32px var(--shadow);
  }
  .brand {
    position: absolute;
    left: 0;
    right: 0;
    top: 276px;
    text-align: center;
    font-weight: 400;
    font-size: 52px;
    line-height: 1;
    letter-spacing: 4px;
    color: var(--brand-light);
  }
  .tagline {
    position: absolute;
    left: 0;
    right: 0;
    top: 336px;
    text-align: center;
    font-weight: 300;
    font-size: 18px;
    letter-spacing: 3px;
    color: var(--tagline);
  }
  .contact {
    position: absolute;
    top: 193px;
    color: var(--ink);
    font-weight: 300;
    font-size: 24.5px;
    line-height: 30px;
    letter-spacing: 0.3px;
  }
  .contact--rotterdam { left: 128px; }
  .contact--amsterdam { left: 426px; }
  .contact__line { display: block; white-space: nowrap; }
  .contact__link {
    display: flex;
    align-items: center;
    gap: 7px;
    margin-top: 12px;
    white-space: nowrap;
  }
  .contact__link svg { flex: none; }
</style>
</head>
<body>
<main class="sheet">
  <section class="card card--front" aria-label="Voorkant">
    <div class="brand">HUIDPUNTZORG</div>
    <div class="tagline">next generation skin care</div>
  </section>

  <section class="card card--back" aria-label="Achterkant">
    <div class="contact contact--rotterdam">
      <span class="contact__line">Lindenhoflaan 214B,</span>
      <span class="contact__line">3041KP Rotterdam,</span>
      <span class="contact__line">P: 010 483 21 95</span>
      <span class="contact__link">
        <svg width="24" height="24" viewBox="0 0 24 24" fill="none" stroke="#1b1b1b" stroke-width="1.1" aria-hidden="true">
          <circle cx="12" cy="12" r="10.5"/>
          <ellipse cx="12" cy="12" rx="4.5" ry="10.5"/>
          <line x1="1.5" y1="12" x2="22.5" y2="12"/>
          <path d="M3.5 6.5h17M3.5 17.5h17"/>
        </svg>
        www.huidpuntzorg.nu
      </span>
    </div>

    <div class="contact contact--amsterdam">
      <span class="contact__line">Zonnewijzerstraat 238,</span>
      <span class="contact__line">1062RT Amsterdam</span>
      <span class="contact__line">P: 020 571 3829</span>
      <span class="contact__link">
        <svg width="28" height="18" viewBox="0 0 28 18" fill="none" stroke="#1b1b1b" stroke-width="1.2" aria-hidden="true">
          <rect x="0.8" y="0.8" width="26.4" height="16.4"/>
          <path d="M0.8 0.8L14 10.5L27.2 0.8M0.8 17.2L10.5 8M27.2 17.2L17.5 8"/>
        </svg>
        info@huidpuntzorg.nu
      </span>
    </div>
  </section>
</main>
</body>
</html>
```